Price Trend Graphic for Estimates

I want to add a graphic to my estimates that shows the projected price trend of the work we are quoting to the customer. I have attached a couple ideas I was working on but they are garbage. Hopefully you can see the intent and make it look a lot better. Basically I want the customer to see a really a professional / technological graphic that will stimulate them to purchase Right Now! before the price goes up further. So maybe if the "Today's Price" looks nice and friendly and then becomes more critical and ominous as it goes forward 30 days.... 90 days.... Idea is to psychologically

Target Market(s)

Customers for our Construction business

Industry/Entity Type

Construction

Colors
0054AA
0677BA
7BADD7
CADEEF
E8F1F8
0094D4
00A9DD
6FCCEA
C7EBF8
E9F6FB
FFF300
FFF600
FEFA6F
FFFEC7
FFFEE8
F0912C
F2A743
F7CA91
FBE8D2
FDF5EE

Requirements
Must have
• nice looking graphic with upwards moving arrow and 3 price points
Nice to have
• technological / modern looking chart

```html
<!DOCTYPE html>
<html lang="en">
<head>
<meta charset="utf-8">
<title>Estimate Price Trend</title>
<link href="https://fonts.googleapis.com/css2?family=Montserrat:wght@400;600;700;800&family=Open+Sans:wght@600&display=swap" rel="stylesheet">
<style>
  :root {
    --page-bg: #ffffff;
    --navy-deep: #0a1748;
    --navy: #10286e;
    --blue: #0054aa;
    --cyan: #00a9dd;
    --cyan-soft: #6fccea;
    --white: #ffffff;
    --point-today: #f2b940;
    --point-30: #f51aa8;
    --point-90: #fcefc0;
    --calendar-red: #e8332b;
    --ink: #111111;
  }
  * { margin: 0; padding: 0; box-sizing: border-box; }
  html, body {
    width: 842px;
    height: 1200px;
    overflow: hidden;
    background: var(--page-bg);
  }
  .canvas {
    position: relative;
    width: 842px;
    height: 1200px;
  }
  .trend-graphic {
    position: absolute;
    left: 31px;
    top: 340px;
    width: 780px;
    height: 519px;
    box-shadow: 0 4px 14px rgba(0,0,0,0.18);
    overflow: hidden;
  }
  .tech-backdrop {
    position: absolute;
    inset: 0;
    background:
      radial-gradient(ellipse 38% 42% at 48% 48%, rgba(0,169,221,0.75), rgba(0,84,170,0) 100%),
      radial-gradient(ellipse 70% 10% at 50% 94%, rgba(111,204,234,0.85), rgba(0,148,212,0) 100%),
      radial-gradient(ellipse 45% 30% at 12% 10%, rgba(111,204,234,0.35), rgba(0,0,0,0) 100%),
      radial-gradient(ellipse 40% 50% at 90% 75%, rgba(0,119,186,0.55), rgba(0,0,0,0) 100%),
      linear-gradient(180deg, var(--navy) 0%, var(--navy-deep) 55%, var(--navy) 100%);
  }
  .trend-chart {
    position: absolute;
    inset: 0;
    width: 100%;
    height: 100%;
  }
  .headline {
    font-family: 'Montserrat', sans-serif;
    font-size: 31px;
    fill: var(--white);
    letter-spacing: 0.5px;
  }
  .headline .strong { font-weight: 800; }
  .headline .light { font-weight: 400; }
  .axis { stroke: var(--white); stroke-width: 3; fill: none; }
  .trend-line { stroke: var(--white); stroke-width: 3.5; fill: none; stroke-linejoin: miter; }
  .leader { stroke: var(--cyan-soft); stroke-width: 1.5; opacity: 0.8; }
  .price {
    font-family: 'Montserrat', sans-serif;
    font-weight: 800;
    font-size: 31px;
    fill: var(--white);
  }
  .point { stroke: var(--white); stroke-width: 4; }
  .point-today { fill: var(--point-today); }
  .point-30 { fill: var(--point-30); }
  .point-90 { fill: var(--point-90); }
  .caption {
    font-family: 'Open Sans', sans-serif;
    font-weight: 600;
    font-size: 18px;
    fill: var(--white);
  }
  .calendar-body { fill: var(--white); stroke: var(--ink); stroke-width: 2.5; }
  .calendar-top { fill: var(--calendar-red); stroke: var(--ink); stroke-width: 2.5; }
  .calendar-ring { fill: none; stroke: var(--ink); stroke-width: 2; }
  .calendar-day {
    font-family: 'Montserrat', sans-serif;
    font-weight: 800;
    font-size: 30px;
    fill: var(--ink);
  }
  .axis-word {
    font-family: 'Montserrat', sans-serif;
    font-weight: 700;
    font-size: 19px;
    fill: var(--white);
  }
  .axis-title {
    font-family: 'Montserrat', sans-serif;
    font-size: 19px;
    fill: var(--white);
    letter-spacing: 4px;
  }
  .axis-title .strong { font-weight: 700; }
  .axis-title .light { font-weight: 400; }
  .corner-bar { fill: var(--white); }
</style>
</head>
<body>
<div class="canvas">
  <section class="trend-graphic">
    <div class="tech-backdrop" role="img" aria-label="Blue technology backdrop with faint stock market candlesticks, grid and light streaks"></div>
    <svg class="trend-chart" viewBox="0 0 1197 797" xmlns="http://www.w3.org/2000/svg">
      <polygon class="corner-bar" points="1063,0 1197,0 1197,16 1080,16"/>
      <polygon class="corner-bar" points="0,786 326,786 338,797 0,797"/>

      <text class="headline" x="599" y="84" text-anchor="middle"><tspan class="strong">SIGNUP</tspan><tspan class="light"> TODAY FOR HUGE </tspan><tspan class="strong">SAVINGS!</tspan></text>

      <polyline class="axis" points="180,113 180,706 1078,706"/>

      <line class="leader" x1="575" y1="283" x2="575" y2="470"/>
      <line class="leader" x1="851" y1="166" x2="851" y2="320"/>

      <polyline class="trend-line" points="180,706 348,498 416,606 575,375 665,523 851,215 920,356 1063,131"/>
      <polygon fill="var(--white)" points="1075,113 1046,130 1070,146"/>

      <circle class="point point-today" cx="348" cy="498" r="25"/>
      <circle class="point point-30" cx="575" cy="375" r="25"/>
      <circle class="point point-90" cx="851" cy="215" r="25"/>

      <text class="price" x="344" y="414" text-anchor="middle">$6,500</text>
      <text class="price" x="573" y="273" text-anchor="middle">$7,280</text>
      <text class="price" x="843" y="157" text-anchor="middle">$7,460</text>

      <text class="caption" x="292" y="572" text-anchor="middle" transform="rotate(-45 292 565)">Today</text>

      <g class="calendar" transform="translate(548,473)">
        <rect class="calendar-body" x="0" y="0" width="55" height="52" rx="5"/>
        <path class="calendar-top" d="M5 0 H50 A5 5 0 0 1 55 5 V11 H0 V5 A5 5 0 0 1 5 0 Z"/>
        <circle class="calendar-ring" cx="13" cy="-2" r="3.5"/>
        <circle class="calendar-ring" cx="23" cy="-2" r="3.5"/>
        <circle class="calendar-ring" cx="33" cy="-2" r="3.5"/>
        <circle class="calendar-ring" cx="43" cy="-2" r="3.5"/>
        <text class="calendar-day" x="27.5" y="44" text-anchor="middle">30</text>
      </g>
      <text class="caption" x="575" y="548" text-anchor="middle">Days</text>

      <g class="calendar" transform="translate(824,322)">
        <rect class="calendar-body" x="0" y="0" width="55" height="52" rx="5"/>
        <path class="calendar-top" d="M5 0 H50 A5 5 0 0 1 55 5 V11 H0 V5 A5 5 0 0 1 5 0 Z"/>
        <circle class="calendar-ring" cx="13" cy="-2" r="3.5"/>
        <circle class="calendar-ring" cx="23" cy="-2" r="3.5"/>
        <circle class="calendar-ring" cx="33" cy="-2" r="3.5"/>
        <circle class="calendar-ring" cx="43" cy="-2" r="3.5"/>
        <text class="calendar-day" x="27.5" y="44" text-anchor="middle">90</text>
      </g>
      <text class="caption" x="854" y="397" text-anchor="middle">Days</text>

      <g class="axis-word" text-anchor="middle">
        <text x="147" y="520">E</text>
        <text x="147" y="553">S</text>
        <text x="147" y="586">T</text>
        <text x="147" y="619">I</text>
        <text x="147" y="652">M</text>
        <text x="147" y="685">A</text>
        <text x="147" y="718">T</text>
        <text x="147" y="751">E</text>
      </g>
      <text class="axis-title" x="179" y="751"><tspan class="strong">PRICE</tspan><tspan class="light"> TREND</tspan></text>
    </svg>
  </section>
</div>
</body>
</html>
```